Edgy rebranded biz cards KRB

We are rebranding our 20 yr old mortgage company with a new logo and would like cards to compliment our new look.

Target Market(s)

potential home buyers or clients for refinance

Industry/Entity Type

Mortgage Brokerage

Contact Information for Business Card

418 W. Lomita Ave #305
Henderson, NV 89152
702.519.4827 o
702-519-4829 f
www.kestrelridgelending,example
nmls 842019
KRB is an equal housing lender

Font styles to use
Sans Serif

Colors
0455a3
3176b5
0393ce
33a6d7

Requirements
Must have
• space for a photo
Nice to have
• One side with the company info and the other with the person's info

```html
<!DOCTYPE html>
<html lang="en">
<head>
<meta charset="utf-8">
<title>Kestrel Ridge Lending — Business Cards</title>
<link rel="stylesheet" href="https://fonts.googleapis.com/css2?family=Montserrat:wght@500;700&family=Lato:wght@400;700&display=swap">
<style>
  :root {
    --brand-blue: #0a78c2;
    --brand-deep: #0455a3;
    --ink-gray: #6b6e72;
    --block-gray: #85878a;
    --photo-tone: #c9ccd0;
    --paper: #ffffff;
    --backdrop: #d3d4cf;
  }
  * { box-sizing: border-box; margin: 0; padding: 0; }
  html, body { width: 1200px; height: 801px; overflow: hidden; }
  body {
    background: var(--backdrop);
    font-family: "Lato", sans-serif;
    position: relative;
  }
  .card {
    position: absolute;
    top: 246px;
    width: 540px;
    height: 309px;
    overflow: hidden;
    box-shadow: 0 6px 18px rgba(0,0,0,.18);
  }
  /* ---------- Front: person side ---------- */
  .card--front { left: 40px; background: var(--paper); }
  .front-brand {
    position: absolute; left: 26px; top: 96px; width: 170px;
    display: flex; align-items: center; gap: 9px;
  }
  .brand-square { width: 13px; height: 13px; background: var(--brand-blue); flex: none; }
  .brand-name {
    font-family: "Montserrat", sans-serif; font-weight: 700;
    color: var(--brand-blue); font-size: 20px; line-height: 1.15;
    text-transform: uppercase; letter-spacing: .4px;
  }
  .front-divider {
    position: absolute; left: 206px; top: 56px; width: 1.5px; height: 140px;
    background: var(--brand-blue);
  }
  .person { position: absolute; left: 222px; top: 40px; width: 224px; }
  .person-name {
    font-family: "Montserrat", sans-serif; font-weight: 700;
    color: var(--brand-blue); font-size: 22px; letter-spacing: .3px;
    white-space: nowrap;
  }
  .person-title { color: var(--ink-gray); font-size: 13px; margin: 2px 0 10px; }
  .contact-list { list-style: none; }
  .contact-list li {
    display: flex; align-items: center; gap: 7px;
    color: var(--ink-gray); font-size: 11px; line-height: 19px;
    white-space: nowrap;
  }
  .contact-list svg { width: 11px; height: 11px; fill: var(--brand-blue); flex: none; }
  .nmls { color: var(--ink-gray); font-size: 12px; margin-top: 4px; padding-left: 18px; }
  .photo-space {
    position: absolute; right: 0; top: 34px; width: 84px; height: 104px;
    background: linear-gradient(180deg, var(--photo-tone), var(--block-gray));
  }
  .housing-badge {
    position: absolute; right: 28px; top: 176px; width: 30px; height: 26px;
    background: var(--brand-blue);
  }
  .address-band {
    position: absolute; left: 0; top: 224px; width: 462px; height: 30px;
    background: var(--brand-blue); color: var(--paper);
    font-family: "Montserrat", sans-serif; font-weight: 500; font-size: 13px;
    display: flex; align-items: center; padding-left: 70px;
  }
  /* ---------- Back: company side ---------- */
  .card--back { left: 620px; background: var(--brand-blue); }
  .back-brand {
    position: absolute; left: 0; right: 0; top: 78px;
    display: flex; justify-content: center; align-items: center; gap: 16px;
  }
  .back-brand .brand-square { width: 22px; height: 22px; background: var(--paper); }
  .back-brand .brand-name { color: var(--paper); font-size: 34px; text-align: center; }
  .back-rule {
    position: absolute; left: 90px; right: 90px; top: 190px; height: 2px;
    background: var(--paper);
  }
  .lender-band {
    position: absolute; left: 0; right: 0; top: 232px; height: 34px;
    background: var(--paper); color: var(--brand-blue);
    font-family: "Lato", sans-serif; font-weight: 700; font-size: 14px;
    letter-spacing: 2px; display: flex; align-items: center; justify-content: center;
  }
</style>
</head>
<body>

<section class="card card--front" aria-label="Business card, person side">
  <div class="front-brand">
    <span class="brand-square"></span>
    <span class="brand-name">Kestrel Ridge Lending</span>
  </div>
  <div class="front-divider"></div>

  <div class="person">
    <h1 class="person-name">DANIEL REYES</h1>
    <p class="person-title">President &amp; CEO</p>
    <ul class="contact-list">
      <li><svg viewBox="0 0 24 24"><path d="M6.6 10.8a15 15 0 0 0 6.6 6.6l2.2-2.2c.3-.3.7-.4 1-.2 1.1.4 2.3.6 3.6.6.6 0 1 .4 1 1V20c0 .6-.4 1-1 1A17 17 0 0 1 3 4c0-.6.4-1 1-1h3.5c.6 0 1 .4 1 1 0 1.3.2 2.5.6 3.6.1.3 0 .7-.2 1z"/></svg>702.519.4827</li>
      <li><svg viewBox="0 0 24 24"><path d="M6 2h10v5H6zM4 8h16a2 2 0 0 1 2 2v7h-4v5H6v-5H2v-7a2 2 0 0 1 2-2zm4 9v3h8v-3z"/></svg>702-519-4829</li>
      <li><svg viewBox="0 0 24 24"><path d="M2 5h20v14H2zm2 2v.5l8 5 8-5V7zm0 3v7h16v-7l-8 5z"/></svg>dreyes@kestrelridgelending.example</li>
      <li><svg viewBox="0 0 24 24"><path d="M12 2a10 10 0 1 0 0 20 10 10 0 0 0 0-20zm0 2c.9 0 2.2 2 2.7 5H9.3C9.8 6 11.1 4 12 4zM4.3 11h3c0 .7 0 1.4.1 2h-3a8 8 0 0 1-.1-2zm5 0h5.4a16 16 0 0 1-.1 2H9.4l-.1-2zm7.4 0h3a8 8 0 0 1-.1 2h-3l.1-2zM9.3 15h5.4c-.5 3-1.8 5-2.7 5s-2.2-2-2.7-5z"/></svg>www.kestrelridgelending.example</li>
    </ul>
    <p class="nmls">NMLS: 842019</p>
  </div>

  <div class="photo-space" role="img" aria-label="Space for the loan officer's portrait photo"></div>
  <div class="housing-badge" role="img" aria-label="Equal housing lender badge"></div>
  <div class="address-band">418 W. Lomita Ave #305 Henderson, NV 89152</div>
</section>

<section class="card card--back" aria-label="Business card, company side">
  <div class="back-brand">
    <span class="brand-square"></span>
    <span class="brand-name">Kestrel Ridge<br>Lending</span>
  </div>
  <div class="back-rule"></div>
  <div class="lender-band">KRB is an Equal Housing Lender</div>
</section>

</body>
</html>
```